Best in class cloud software provider for retailers needs a new business card design to reflect prod

We are a software company based out of Chicago selling into retailers. We have a new website and marketing collateral that support our new product designs. We are obsessed with simplicity, ease of use, and having a really powerful product set. We have two products as noted on our website - www.brolvane.com - one is a retail task management product and the other is a Help Ticketing product.

At Brolvane we are passionate about creating the best Retail Task Management system in the industry. We bring more than 20 years of retail operations, Workforce Management and Retail Task experience and have a set of web and mobile software features that no one else has. Brolvane enables you to plan and distribute work throughout your organization and ensure it gets done.

We need a new business card design that reflects our new branding, message and approach.

I've attached a few documents that help support what we are building and how our colors look.

There may be additional future work if this goes well.

Thanks,
Mark

President

Target Market(s)

We sell into retailers and are a software company

Industry/Entity Type

Software

Contact Information for Business Card

The card must have

Name
title
address
tele
email
Brolvane logo (someplace)

So for example

It would have for me

Mark Dorsett
President
48 West Harlow Ave. Suite 310
Chicago, IL 60687
3125550187
mdorsett@brolvane.com

Requirements
Must have
• We need to cards for 5 different people - same design different names etc
Nice to have
• should reflect our colors and product and website - be creative - ease of use, simplicity, and power is what the product is about - but we are very forward Brolvane and hear all the time that our product is gorgeous. The font should be consistent with our website, and marketing one pager included
Should not have
• Strange or unfamiliar colors or fonts...

```html
<!DOCTYPE html>
<html lang="en">
<head>
<meta charset="utf-8">
<title>Brolvane Business Card</title>
<link rel="stylesheet" href="https://fonts.googleapis.com/css2?family=Open+Sans:wght@400;600;700&display=swap">
<style>
  :root {
    --brand-orange: #f26a2c;
    --card-white: #ffffff;
    --ink: #1c1c1c;
    --backdrop: #ebe7e3;
  }
  * { box-sizing: border-box; margin: 0; padding: 0; }
  html, body { width: 1200px; height: 900px; overflow: hidden; }
  body {
    background: var(--backdrop);
    font-family: "Open Sans", Arial, sans-serif;
    position: relative;
  }
  .card {
    position: absolute;
    border-radius: 14px;
    overflow: hidden;
    box-shadow: 0 6px 18px rgba(0,0,0,0.12);
  }
  .card-front {
    left: 78px; top: 35px; width: 588px; height: 363px;
    background: var(--card-white);
  }
  .card-back {
    left: 390px; top: 507px; width: 565px; height: 348px;
    background: var(--brand-orange);
  }
  .brand-band {
    position: absolute; left: 0; right: 0;
    height: 99px;
    display: flex; align-items: center;
  }
  .card-front .brand-band { top: 28px; background: var(--brand-orange); }
  .card-back .brand-band { top: 105px; background: var(--card-white); }
  .brand-pill {
    position: absolute; top: 0; height: 99px;
    border-radius: 50px;
    display: flex; align-items: center; justify-content: center;
  }
  .card-front .brand-pill { left: 100px; width: 392px; background: var(--card-white); }
  .card-back .brand-pill { left: 60px; width: 438px; background: var(--brand-orange); }
  .brand-name {
    font-weight: 700;
    font-size: 60px;
    letter-spacing: -0.5px;
    line-height: 1;
  }
  .card-front .brand-name { color: var(--brand-orange); }
  .card-back .brand-name { color: var(--card-white); font-size: 66px; }
  .contact {
    position: absolute; left: 0; right: 0; top: 160px;
    text-align: center; color: var(--ink);
  }
  .person-name {
    color: var(--brand-orange); font-weight: 600; font-size: 21px; line-height: 28px;
  }
  .person-title { font-size: 16px; line-height: 26px; }
  .contact-line {
    font-size: 16px; line-height: 24px;
    display: flex; align-items: center; justify-content: center; gap: 5px;
  }
  .contact-line svg { fill: var(--brand-orange); }
  .phone-line { margin-top: 24px; }
  .address-line { margin-top: 24px; font-size: 16px; }
</style>
</head>
<body>
  <section class="card card-front">
    <div class="brand-band">
      <div class="brand-pill"><span class="brand-name">Brolvane</span></div>
    </div>
    <div class="contact">
      <p class="person-name">Mark Dorsett</p>
      <p class="person-title">President</p>
      <p class="contact-line phone-line">
        <svg width="11" height="11" viewBox="0 0 24 24" aria-hidden="true"><path d="M6.6 10.8a15.1 15.1 0 0 0 6.6 6.6l2.2-2.2a1 1 0 0 1 1-.25 11.4 11.4 0 0 0 3.6.57 1 1 0 0 1 1 1V20a1 1 0 0 1-1 1A17 17 0 0 1 3 4a1 1 0 0 1 1-1h3.5a1 1 0 0 1 1 1c0 1.25.2 2.45.57 3.57a1 1 0 0 1-.25 1z"/></svg>
        3125550187
      </p>
      <p class="contact-line">
        <svg width="12" height="9" viewBox="0 0 24 18" aria-hidden="true"><path d="M0 0h24v2L12 9 0 2z M0 4.5l12 7 12-7V18H0z"/></svg>
        mdorsett@brolvane.com
      </p>
      <p class="address-line">48 West Harlow Ave. Suite 310 Chicago, IL 60687</p>
    </div>
  </section>

  <section class="card card-back">
    <div class="brand-band">
      <div class="brand-pill"><span class="brand-name">Brolvane</span></div>
    </div>
  </section>
</body>
</html>
```